Brenton Civil

We need a Standard Professional Company Letterhead, company standard document template, coversheet template for a civil construction company. We would like the designs to use the company colour red

I have attached existing templates that need to improve greatly but please use as a quide of general layout.

```html
<!DOCTYPE html>
<html lang="en">
<head>
<meta charset="utf-8">
<title>Brenton Civil — Letterhead</title>
<link rel="stylesheet" href="https://fonts.googleapis.com/css2?family=Montserrat:wght@400;500;600&family=Poppins:wght@400;500;600&display=swap">
<style>
  :root {
    --brand-red: #c8202f;
    --ink: #2b2b2b;
    --body-grey: #6b6b6b;
    --band-grey: #e6e6e6;
    --paper: #ffffff;
    --backdrop: #eceef0;
  }
  * { box-sizing: border-box; margin: 0; padding: 0; }
  html, body { width: 1200px; height: 1200px; overflow: hidden; }
  body {
    background: var(--backdrop);
    font-family: "Montserrat", Arial, sans-serif;
    position: relative;
  }
  .letterhead {
    position: absolute;
    left: 175px; top: 50px;
    width: 850px; height: 1100px;
    background: var(--paper);
    box-shadow: 0 6px 24px rgba(0,0,0,0.12);
  }
  .corner-block {
    position: absolute; left: 0; top: 0;
    width: 34px; height: 78px;
    background: var(--brand-red);
  }
  .brand {
    position: absolute; left: 60px; top: 40px;
    display: flex; align-items: center; gap: 12px;
  }
  .brand-dot {
    width: 40px; height: 40px; border-radius: 50%;
    background: var(--brand-red);
  }
  .brand-name {
    font-family: "Poppins", Arial, sans-serif;
    font-weight: 500; font-size: 22px; letter-spacing: 1px;
    color: var(--brand-red); text-transform: uppercase;
  }
  .contact {
    position: absolute; right: 40px; top: 40px;
    list-style: none; text-align: right;
    font-size: 11px; color: var(--body-grey);
  }
  .contact li { display: flex; align-items: center; justify-content: flex-end; gap: 8px; margin-bottom: 6px; }
  .contact svg { width: 16px; height: 16px; }
  .recipient {
    position: absolute; left: 70px; top: 150px;
    font-family: "Poppins", Arial, sans-serif; color: var(--ink);
    font-size: 11px; line-height: 1.45;
  }
  .recipient .to { font-size: 11px; color: var(--body-grey); }
  .recipient .name { font-size: 19px; font-weight: 600; line-height: 1.2; }
  .recipient b { font-weight: 600; }
  .body-text {
    position: absolute; left: 70px; top: 290px; width: 650px;
    font-size: 12.5px; line-height: 1.75; color: var(--body-grey);
  }
  .body-text p { margin-bottom: 22px; }
  .sign-off { position: absolute; left: 70px; top: 790px; }
  .signature {
    width: 150px; height: 70px; border-radius: 6px;
    background: linear-gradient(135deg, #d9d9d9, #bdbdbd);
  }
  .designation {
    margin-top: 14px; font-size: 11px; letter-spacing: 4px;
    color: var(--body-grey); text-transform: uppercase;
  }
  .footer {
    position: absolute; left: 0; bottom: 40px; width: 100%; height: 42px;
    display: flex;
  }
  .footer-address {
    flex: 0 0 76%; background: var(--brand-red); color: #fff;
    display: flex; align-items: center; padding-left: 40px;
    font-size: 12px; letter-spacing: 0.6px; text-transform: uppercase;
  }
  .footer-address b { font-weight: 600; margin-right: 4px; }
  .footer-abn {
    flex: 1; background: var(--band-grey); color: var(--ink);
    display: flex; align-items: center; justify-content: center;
    font-family: "Poppins", Arial, sans-serif; font-size: 13px;
  }
  .footer-abn b { font-weight: 600; margin-right: 5px; }
</style>
</head>
<body>
  <main class="letterhead">
    <div class="corner-block"></div>

    <div class="brand">
      <span class="brand-dot"></span>
      <span class="brand-name">Brenton Civil</span>
    </div>

    <ul class="contact">
      <li>daniel@brentoncivil.com.au
        <svg viewBox="0 0 16 16"><circle cx="8" cy="8" r="7" fill="none" stroke="var(--brand-red)" stroke-width="1.2"/><rect x="4.2" y="5.3" width="7.6" height="5.4" fill="var(--brand-red)"/><path d="M4.2 5.3 L8 8.3 L11.8 5.3" fill="none" stroke="#fff" stroke-width="0.8"/></svg>
      </li>
      <li>042 5510 734
        <svg viewBox="0 0 16 16"><circle cx="8" cy="8" r="7" fill="none" stroke="var(--brand-red)" stroke-width="1.2"/><path d="M5.5 4.5 L7 4.5 L7.6 6.4 L6.7 7.2 Q7.6 8.9 9 9.5 L9.8 8.6 L11.5 9.2 L11.5 10.6 Q8.5 11 6.5 9 Q4.6 7 5.5 4.5 Z" fill="var(--brand-red)"/></svg>
      </li>
    </ul>

    <section class="recipient">
      <div class="to">To</div>
      <div class="name">Liam Carter</div>
      <div>CEO, NORTHWAY STUDIO</div>
      <div><b>M:</b> +91 70215 43680</div>
      <div><b>Date:</b> 24-03-2018</div>
    </section>

    <section class="body-text">
      <p>Lorem ipsum dolor sit amet, consectetur adipiscing elit. Pellentesque dictum, ante non ullamcorper convallis, nunc quam blandit metus, ac mollis eros felis a orci. Donec congue, mauris ut pulvinar lobortis, dolor massa feugiat nisi, at tincidunt metus leo vel elit. Proin facilisis semper lobortis. Vivamus augue purus, cursus quis urna non, accumsan pellentesque est. Nulla in iaculis magna, quis aliquet ex. Cras efficitur metus eget purus euismod facilisis. Proin non metus tincidunt, auctor ipsum a, tempor mi.</p>
      <p>Nulla egestas vulputate risus, ut vestibulum diam commodo id. Mauris ornare libero eu erat porttitor ultrices. Proin sed lectus scelerisque ligula bibendum sagittis ac nec leo. Donec ac accumsan diam, et lobortis mauris.</p>
      <p>Nulla congue volutpat nisl ac lobortis. Integer dignissim interdum libero, quis feugiat velit pretium at. Phasellus sit amet libero rutrum, feugiat odio et, tempus purus. Cras ultricies, leo at fringilla sollicitudin, leo sapien placerat enim, a rutrum lorem enim ut tortor. Phasellus magna ante, congue maximus egestas sit amet, venenatis scelerisque felis.</p>
      <p>Nulla congue volutpat nisl ac lobortis. Integer dignissim interdum libero, quis feugiat velit pretium at. Phasellus sit amet libero rutrum, feugiat odio et, tempus purus. Cras ultricies, leo at fringilla sollicitudin, leo sapien placerat enim, a rutrum lorem enim ut tortor. Phasellus magna ante, congue maximus egestas sit amet, venenatis scelerisque felis.</p>
    </section>

    <section class="sign-off">
      <div class="signature" role="img" aria-label="Handwritten signature of the sender"></div>
      <div class="designation">[ Designation ]</div>
    </section>

    <footer class="footer">
      <div class="footer-address"><b>A:</b> PO Box 52, Riverton QLD 4720, <b>&nbsp;W:</b> brentoncivil.com.au</div>
      <div class="footer-abn"><b>ABN</b> 31 584 207 615</div>
    </footer>
  </main>
</body>
</html>
```